Need web design for our e-assessment company

We need a web design for our e-assessment company called Tavelo. We develop modern, web-based software for supporting the testing and examination process. The application is delivered as a SaaS solution.

The application helps our customers save time and money.

The design should communicate the following:

- Modern
- Innovation
- Security
- Performance

Attached you can find a screenshot of our application as well as some thoughts on the website.

We would like a front page as well as 1 sub page.

And lastly, one more website we draw inspiration from (on top of the ones mentioned in the attached document): http://www.plonkavery.example/
Updates

Dear all,

I have updated the description with 1 more example of websites we like as well as added that we would like a front page and a sub page.

Thanks in advance.

Best regards,

Torlak

Target Market(s)

Our target groups are higher education and awarding organisations. Decision makers are mostly men age 45+.

Industry/Entity Type

It Company

Requirements
Must have
• 1 front page and 1 sub page

```html
<!DOCTYPE html>
<html lang="en">
<head>
<meta charset="utf-8">
<title>Tavelo – e-Assessment Simplified</title>
<link href="https://fonts.googleapis.com/css2?family=Didact+Gothic&family=Open+Sans:wght@400;600;700&family=Kaushan+Script&display=swap" rel="stylesheet">
<style>
:root{
  --orange:#f26a21;
  --blue:#1aa6e4;
  --ink:#3a3a3a;
  --muted:#8a8a8a;
  --line:#d9d9d9;
  --band:#e6e6e6;
  --band-light:#f1f1f1;
  --white:#ffffff;
  --dark:#2b2d33;
}
*{box-sizing:border-box;margin:0;padding:0}
html,body{width:1200px;height:3444px;overflow:hidden;background:var(--white)}
body{font-family:"Open Sans",Arial,sans-serif;color:var(--ink);position:relative}
.heading{font-family:"Didact Gothic","Century Gothic",sans-serif;font-weight:400;color:var(--ink)}
.script{font-family:"Kaushan Script",cursive}
.btn{display:inline-block;border-radius:4px;color:var(--white);font-weight:600;text-align:center}
.btn-blue{background:var(--blue)}
.btn-orange{background:var(--orange)}
p.copy{font-size:15px;line-height:22px;color:var(--muted)}

/* header */
.site-header{position:absolute;top:0;left:0;width:1200px;height:80px;background:var(--white);border-bottom:1px solid var(--line)}
.brand{position:absolute;left:44px;top:20px;display:flex;align-items:center;gap:12px}
.brand-dot{width:40px;height:40px;border-radius:50%;background:var(--orange)}
.brand-name{font-family:"Didact Gothic",sans-serif;font-size:28px;color:var(--ink)}
.main-nav{position:absolute;right:44px;top:30px;display:flex;gap:40px;font-size:14px;font-weight:600;color:var(--ink)}

/* hero */
.hero{position:absolute;top:80px;left:0;width:1200px;height:560px;background:linear-gradient(120deg,#3b3330 0%,#6b5a4e 45%,#8d7b6c 70%,#4a413b 100%)}
.hero-panel{position:absolute;left:48px;top:0;width:352px;height:330px;background:rgba(242,106,33,.92);border-radius:0 0 14px 14px;padding:26px 30px}
.hero-item{display:flex;align-items:center;gap:26px;height:96px;color:var(--white);font-size:22px}
.hero-title{position:absolute;left:610px;top:24px;font-size:44px;color:var(--white)}
.hero-cta{position:absolute;left:684px;top:92px;width:188px;height:48px;line-height:48px;font-size:19px}
.hero-laptop{position:absolute;left:560px;top:160px;width:540px;height:360px;background:linear-gradient(180deg,#e8eef3,#b7c2cc);border-radius:10px 10px 4px 4px}

/* demo band */
.demo-band{position:absolute;top:640px;left:0;width:1200px;height:200px;background:var(--band)}
.demo-text{position:absolute;left:48px;top:64px;font-size:38px;color:#555}
.demo-cta{position:absolute;left:560px;top:64px;width:220px;height:52px;line-height:52px;font-size:19px}
.social{position:absolute;right:60px;top:68px;display:flex;gap:26px}
.social span{width:40px;height:40px;border-radius:50%;background:#a8a8a8}

/* how it works */
.how{position:absolute;top:860px;left:0;width:1200px;height:340px}
.how h2{position:absolute;left:48px;top:10px;font-size:42px}
.how .copy-block{position:absolute;left:48px;top:80px;width:540px}
.how .copy-block p+p{margin-top:16px}
.watch{position:absolute;left:48px;top:266px;font-size:30px;color:var(--orange)}
.video{position:absolute;left:700px;top:10px;width:340px;height:260px;background:#dcdcdc}
.video-bar{position:absolute;left:0;bottom:0;width:340px;height:32px;background:#3d3d3d}

/* features */
.features{position:absolute;top:1220px;left:0;width:1200px;height:420px;background:var(--band-light)}
.monitor{position:absolute;left:150px;top:100px;width:440px;height:300px;background:linear-gradient(180deg,#f4f6f8,#c9d0d6);border-radius:6px}
.features h2{position:absolute;left:700px;top:76px;font-size:38px}
.feature-list{position:absolute;left:700px;top:146px;list-style:none}
.feature-list li{display:flex;align-items:center;gap:16px;height:48px;font-size:17px}
.feature-list li i{width:28px;height:28px;border-radius:50%;background:var(--orange)}

/* case studies */
.cases{position:absolute;top:1720px;left:0;width:1200px;height:320px}
.cases h2{position:absolute;left:48px;top:12px;font-size:36px}
.case{position:absolute;top:110px;width:440px;display:flex;gap:26px}
.case-body{flex:1;min-width:0}
.case-photo{width:140px;height:140px;border-radius:50%;flex:none}
.case-name{font-size:14px;font-weight:700;margin:6px 0 8px}
.case-name b{color:var(--orange)}
.read-more{font-size:13px;color:var(--orange);margin-top:6px}

/* partners */
.partners{position:absolute;top:2060px;left:0;width:1200px;height:200px;background:var(--band-light)}
.partners h2{position:absolute;left:48px;top:16px;font-size:34px}
.partner-row{position:absolute;left:48px;top:100px;width:1104px;display:flex;justify-content:space-between;align-items:center;font-family:"Didact Gothic",sans-serif;font-size:40px;color:#444}

/* blog */
.blog{position:absolute;top:2290px;left:0;width:1200px;height:290px}
.blog h2{position:absolute;left:48px;top:10px;font-size:36px}
.blog-all{position:absolute;right:48px;top:24px;font-size:13px;color:var(--muted)}
.post{position:absolute;top:96px;width:500px;display:flex;gap:30px}
.post-body{flex:1;min-width:0}
.date{width:170px;height:170px;border-radius:50%;background:var(--orange);color:var(--white);text-align:center;font-family:"Didact Gothic",sans-serif;flex:none;padding-top:30px;line-height:36px;font-size:38px}
.post-title{font-size:14px;font-weight:700;margin:10px 0 8px}
.post-title b{color:var(--orange)}

/* get started */
.start{position:absolute;top:2600px;left:0;width:1200px;height:270px;background:linear-gradient(110deg,#22252c,#3e4350 50%,#2a2d35)}
.start p{position:absolute;left:0;top:46px;width:1200px;text-align:center;color:var(--white);font-size:32px;line-height:42px}
.start-cta{position:absolute;left:500px;top:160px;width:300px;height:56px;line-height:56px;font-size:24px;font-weight:400}

/* footer */
.site-footer{position:absolute;top:2870px;left:0;width:1200px;height:510px;background:var(--band)}
.col{position:absolute;top:40px;width:320px}
.col h3{font-family:"Didact Gothic",sans-serif;font-weight:400;font-size:24px;padding-bottom:12px;border-bottom:1px solid #c4c4c4;margin-bottom:18px}
.field{width:240px;height:40px;background:var(--white);border:1px solid #ccc;margin-bottom:14px;font-size:13px;color:#999;padding:10px 12px}
.field.area{height:130px}
.send{width:110px;height:34px;line-height:34px;background:#bdbdbd;font-size:13px;color:var(--white);text-align:center}
.tweet{display:flex;gap:14px;margin-bottom:24px}
.tweet i{width:26px;height:26px;border-radius:50%;background:#a8a8a8;flex:none;margin-top:4px}
.tweet small{display:block;color:var(--orange);font-size:13px;margin-top:6px}
.social-sm{display:flex;gap:10px;margin-top:16px}
.social-sm span{width:30px;height:30px;border-radius:50%;border:2px solid #888}
.bottom-bar{position:absolute;top:3380px;left:0;width:1200px;height:64px;background:var(--band);border-top:1px solid #c9c9c9;font-size:13px;color:var(--muted)}
.bottom-bar .left{position:absolute;left:48px;top:22px}
.bottom-bar .mid{position:absolute;left:460px;top:22px}
.bottom-bar svg{position:absolute;right:48px;top:18px}
</style>
</head>
<body>

<header class="site-header">
  <div class="brand"><span class="brand-dot"></span><span class="brand-name">Tavelo</span></div>
  <nav class="main-nav"><span>HOME</span><span>ABOUT US</span><span>SERVICES</span><span>SOFTWARE</span><span>FEATURES</span><span>CONTACT US</span></nav>
</header>

<section class="hero" role="img" aria-label="Blurred café scene with a laptop showing the assessment dashboard">
  <div class="hero-panel">
    <div class="hero-item">
      <svg width="60" height="60" viewBox="0 0 60 60"><rect x="14" y="12" width="32" height="36" rx="3" fill="none" stroke="#fff" stroke-width="4"/><line x1="20" y1="24" x2="40" y2="24" stroke="#fff" stroke-width="3"/><line x1="20" y1="34" x2="40" y2="34" stroke="#fff" stroke-width="3"/><line x1="6" y1="54" x2="54" y2="6" stroke="#fff" stroke-width="5"/></svg>
      <span>No servers.</span>
    </div>
    <div class="hero-item">
      <svg width="60" height="60" viewBox="0 0 60 60"><circle cx="30" cy="30" r="14" fill="none" stroke="#fff" stroke-width="5"/><circle cx="30" cy="30" r="5" fill="#fff"/><line x1="6" y1="54" x2="54" y2="6" stroke="#fff" stroke-width="5"/></svg>
      <span>No maintenance.</span>
    </div>
    <div class="hero-item">
      <svg width="60" height="60" viewBox="0 0 60 60"><circle cx="30" cy="30" r="20" fill="none" stroke="#fff" stroke-width="4"/><circle cx="23" cy="25" r="2.5" fill="#fff"/><circle cx="37" cy="25" r="2.5" fill="#fff"/><path d="M21 40 Q30 33 39 40" fill="none" stroke="#fff" stroke-width="3"/><line x1="6" y1="54" x2="54" y2="6" stroke="#fff" stroke-width="5"/></svg>
      <span>No worries.</span>
    </div>
  </div>
  <div class="hero-title script">e-Assessment. Simplified</div>
  <span class="btn btn-blue hero-cta">TRY IT NOW!</span>
  <div class="hero-laptop" role="img" aria-label="Laptop displaying the Tavelo dashboard"></div>
</section>

<section class="demo-band">
  <div class="demo-text">Sign up for a free demo</div>
  <span class="btn btn-orange demo-cta">SIGN UP NOW!</span>
  <div class="social"><span></span><span></span><span></span></div>
</section>

<section class="how">
  <h2 class="heading">How it Works</h2>
  <div class="copy-block">
    <p class="copy">Etiam mattis tellus ut eleifend semper. Integer a velit urna. Cras mollis urna non lorem, at iaculis odio semper. Donec posuere ante arcu, vitae blandit sem euismod vel. In hendrerit purus nec lacus cursus, eget fermentum enim tristique. Sed at nisl non risus.</p>
    <p class="copy">Nullam porta mi in nibh tincidunt, quis tempus felis sodales. Vivamus at ligula sapien. Aenean vitae sem ut libero gravida.</p>
  </div>
  <div class="watch script">Watch the video
    <svg width="300" height="20" viewBox="0 0 300 20" style="vertical-align:middle"><path d="M4 14 Q150 4 290 10" fill="none" stroke="#bbb" stroke-width="2"/><path d="M280 4 L292 10 L280 16" fill="none" stroke="#bbb" stroke-width="2"/></svg>
  </div>
  <div class="video">
    <svg width="340" height="228" viewBox="0 0 340 228"><circle cx="170" cy="114" r="34" fill="none" stroke="#fff" stroke-width="5"/><path d="M160 96 L188 114 L160 132 Z" fill="#fff"/></svg>
    <div class="video-bar">
      <svg width="340" height="32" viewBox="0 0 340 32"><path d="M12 9 L24 16 L12 23 Z" fill="#ddd"/><rect x="40" y="14" width="220" height="4" fill="#777"/><rect x="280" y="12" width="40" height="8" fill="#777"/></svg>
    </div>
  </div>
</section>

<section class="features">
  <div class="monitor" role="img" aria-label="Desktop monitor showing assessment reports"></div>
  <h2 class="heading">FEATURES</h2>
  <ul class="feature-list">
    <li><i></i>Create Questions</li>
    <li><i></i>Create Assessments</li>
    <li><i></i>Schedule Assessments</li>
    <li><i></i>Deliver Assessments to Candidates</li>
    <li><i></i>Mark Those Assessments</li>
  </ul>
</section>

<section class="cases">
  <h2 class="heading">CASE STUDIES</h2>
  <article class="case" style="left:150px">
    <div class="case-photo" role="img" aria-label="Portrait of a client" style="background:linear-gradient(160deg,#d8d8d8,#9a9a9a)"></div>
    <div class="case-body">
      <div class="case-name"><b>Jonas Berg</b> – www.clientsite.example</div>
      <p class="copy">Donec mattis tellus ut eleifend semper. Integer a velit urna. Cras mollis urna non lorem, at iaculis odio semper.</p>
      <div class="read-more">READ MORE »</div>
    </div>
  </article>
  <article class="case" style="left:630px">
    <div class="case-photo" role="img" aria-label="Portrait of a client" style="background:linear-gradient(160deg,#c9b8aa,#6e5a4c)"></div>
    <div class="case-body">
      <div class="case-name"><b>Mia Lorens</b> – www.clientsite.example</div>
      <p class="copy">Donec mattis tellus ut eleifend semper. Integer a velit urna. Cras mollis urna non lorem, at iaculis odio semper.</p>
      <div class="read-more">READ MORE »</div>
    </div>
  </article>
</section>

<section class="partners">
  <h2 class="heading">OUR PARTNERS</h2>
  <div class="partner-row"><span>Fernmark</span><span>QTR</span><span>Weekday Ledger</span><span>Kestrel Post</span><span>VANTRO</span></div>
</section>

<section class="blog">
  <h2 class="heading">OUR RECENT BLOG / NEWS</h2>
  <div class="blog-all">View all blog / news</div>
  <article class="post" style="left:100px">
    <div class="date">20<br>MAY<br>14</div>
    <div class="post-body">
      <div class="post-title">Donec posuere ante vel | <b>Author Name</b></div>
      <p class="copy">Etiam mattis tellus ut eleifend semper. Integer a velit urna. Cras mollis urna non lorem, at iaculis odio semper.</p>
      <div class="read-more">READ MORE »</div>
    </div>
  </article>
  <article class="post" style="left:640px">
    <div class="date">01<br>JUNE<br>14</div>
    <div class="post-body">
      <div class="post-title">Donec posuere ante vel | <b>Author Name</b></div>
      <p class="copy">Etiam mattis tellus ut eleifend semper. Integer a velit urna. Cras mollis urna non lorem, at iaculis odio semper.</p>
      <div class="read-more">READ MORE »</div>
    </div>
  </article>
</section>

<section class="start" role="img" aria-label="Dim photo of people working at laptops">
  <p>Etiam mattis tellus ut eleifend semper. Integer a velit urna. Cras mollis<br>urna non lorem, at iaculis odio semper.</p>
  <span class="btn btn-blue start-cta">Getting Started</span>
</section>

<footer class="site-footer">
  <div class="col" style="left:48px">
    <h3>ABOUT TAVELO</h3>
    <p class="copy">Lorem ipsum dolor sit amet, consectetur adipiscing elit. Donec posuere ante arcu, vitae blandit sem euismod vel.</p>
    <p class="copy" style="margin-top:14px">Nullam porta mi in nibh tincidunt, quis tempus felis sodales vitae.</p>
    <div class="social-sm"><span></span><span></span><span></span></div>
  </div>
  <div class="col" style="left:440px">
    <h3>CONTACT FORM</h3>
    <div class="field">Name</div>
    <div class="field">Email</div>
    <div class="field">Phone</div>
    <div class="field area">Message</div>
    <div class="send">SEND</div>
  </div>
  <div class="col" style="left:800px">
    <h3>RECENT TWEETS</h3>
    <div class="tweet"><i></i><p class="copy">Integer a velit urna. Cras mollis urna non lorem, at iaculis odio.<small>2 days ago</small></p></div>
    <div class="tweet"><i></i><p class="copy">Donec posuere ante arcu, vitae blandit sem euismod vel.<small>2 days ago</small></p></div>
    <div class="tweet"><i></i><p class="copy">Nullam porta mi in nibh tincidunt, quis tempus felis.<small>2 days ago</small></p></div>
  </div>
</footer>

<div class="bottom-bar">
  <span class="left">Copyright © 2014 TAVELO</span>
  <span class="mid">Terms &amp; Conditions | Privacy Policy</span>
  <svg width="28" height="28" viewBox="0 0 28 28"><path d="M6 18 L14 8 L22 18" fill="none" stroke="#333" stroke-width="4"/></svg>
</div>

</body>
</html>
```